Marisella Crowe Photography

I am looking for someone to design a business card for me. I am a newborn and children's photographer. I want the card to have the proper contact information on it, but I want it to have a soft, simplistic, dreamy type of feel to attract moms. I would love to include soft colors. Maybe lavenders or pinks etc...

I have already had the logo designed and would like it incorporated into my business card.

I have uploaded a couple of the photo's I would like to use on the card. Feel free to use just one or both of them. Or however you see fit. The most important thing is for the card to have the feel i am looking for.

Thank you!

Target Market(s)

families and pregnant women looking for photography services.

Industry/Entity Type

Business

Font styles to use
Sans Serif
Other font styles liked:
• whatever fonts look light and whimsy, but easy to read

Colors
8869ae
eea4c8
86cae6
d2a4cc
e34197
86cfc6

Requirements
Must have
• www.marisellacrowephotography-example.com
www.socialpage-example.com/marisellacrowephotography
marisella@marisellacrowephotography-example.com
555-392-1846
Should not have
• any masculine components i.e. dark colors, square boxes etc...

```html
<!DOCTYPE html>
<html lang="en">
<head>
<meta charset="utf-8">
<title>Marisella Crowe Photography – Business Card</title>
<link rel="stylesheet" href="https://fonts.googleapis.com/css2?family=Arimo:wght@400;700&family=Poiret+One&display=swap">
<style>
  :root {
    --backdrop: #ece6ea;
    --pink-light: #f6dcea;
    --pink-mid: #efc4dc;
    --pink-deep: #e7a9c9;
    --mauve-band: rgba(190, 120, 160, 0.55);
    --lavender: #8869ae;
    --ink: #2a1f2e;
    --white: #ffffff;
    --card-w: 720px;
    --card-h: 411px;
  }
  * { box-sizing: border-box; margin: 0; padding: 0; }
  html, body { width: 1200px; height: 900px; overflow: hidden; }
  body {
    background: var(--backdrop);
    font-family: "Arimo", Arial, sans-serif;
    display: flex;
    flex-direction: column;
    align-items: center;
    justify-content: center;
    gap: 30px;
  }
  .card {
    position: relative;
    width: var(--card-w);
    height: var(--card-h);
    overflow: hidden;
    box-shadow: 0 6px 18px rgba(80, 40, 70, 0.18);
  }
  .card__bokeh {
    position: absolute; inset: 0;
    background: linear-gradient(135deg, var(--pink-light) 0%, var(--pink-mid) 55%, var(--pink-light) 100%);
  }

  /* Front */
  .front__circle {
    position: absolute;
    left: 150px; top: -40px;
    width: 420px; height: 420px;
    border-radius: 50%;
    background: rgba(240, 180, 215, 0.55);
  }
  .brand {
    position: absolute;
    left: 0; right: 0;
    text-align: center;
    color: var(--lavender);
    font-weight: 400;
  }
  .front .brand {
    top: 120px;
    font-size: 38px;
    line-height: 1.15;
  }
  .front .brand span { display: block; font-size: 24px; letter-spacing: 3px; }
  .front__links {
    position: absolute;
    left: 0; right: 0; top: 265px;
    text-align: center;
    color: var(--ink);
    font-weight: 700;
    font-size: 17px;
    line-height: 1.5;
  }
  .front__social { display: inline-flex; align-items: center; gap: 8px; }
  .front__social i {
    display: inline-block; width: 14px; height: 14px;
    border-radius: 50%;
    background: var(--lavender);
  }

  /* Back */
  .back .brand {
    top: 30px; left: auto; right: 40px;
    text-align: right;
    font-size: 24px;
  }
  .back .brand span { display: block; font-size: 14px; letter-spacing: 2px; }
  .back__band {
    position: absolute;
    left: 0; right: 0; top: 160px; bottom: 0;
    background: var(--mauve-band);
  }
  .back__band-glow {
    position: absolute; inset: 0;
    background: linear-gradient(180deg, rgba(231,169,201,0.2), rgba(227,65,151,0.18) 40%, rgba(246,220,234,0.25));
  }
  .back__details {
    position: absolute;
    left: 36px; top: 215px;
    color: var(--white);
  }
  .back__name {
    font-family: "Poiret One", "Arimo", sans-serif;
    font-size: 34px;
    letter-spacing: 2px;
    text-transform: uppercase;
    margin-bottom: 8px;
  }
  .contact {
    list-style: none;
    font-size: 19px;
    line-height: 1.65;
  }
  .contact li { display: flex; align-items: center; gap: 12px; }
  .contact svg { width: 20px; height: 20px; flex: none; }
</style>
</head>
<body>

  <section class="card front" aria-label="Business card front">
    <div class="card__bokeh" role="img" aria-label="Soft pink bokeh light background"></div>
    <div class="front__circle"></div>
    <p class="brand">Marisella Crowe<span>Photography</span></p>
    <div class="front__links">
      <p>www.marisellacrowephotography-example.com</p>
      <p class="front__social"><i></i>www.socialpage-example.com/marisellacrowephotography</p>
    </div>
  </section>

  <section class="card back" aria-label="Business card back">
    <div class="card__bokeh" role="img" aria-label="Soft pink bokeh light background"></div>
    <p class="brand">Marisella Crowe<span>Photography</span></p>
    <div class="back__band">
      <div class="back__band-glow" role="img" aria-label="Blurred pink bokeh lights"></div>
    </div>
    <div class="back__details">
      <h1 class="back__name">Marisella Crowe</h1>
      <ul class="contact">
        <li>
          <svg viewBox="0 0 20 20" aria-hidden="true"><path fill="#fff" d="M2 7c0-2 3-3 8-3s8 1 8 3v2h-4V7.5C12.5 7 7.5 7 6 7.5V9H2zM5 10h10l2 7H3z"/></svg>
          555-392-1846
        </li>
        <li>
          <svg viewBox="0 0 20 20" aria-hidden="true"><rect x="1.5" y="4.5" width="17" height="11" fill="none" stroke="#fff" stroke-width="1.6"/><path d="M2 5l8 6 8-6" fill="none" stroke="#fff" stroke-width="1.6"/></svg>
          marisella@marisellacrowephotography-example.com
        </li>
        <li>
          <svg viewBox="0 0 20 20" aria-hidden="true"><g fill="none" stroke="#fff" stroke-width="1.4"><circle cx="10" cy="10" r="8"/><ellipse cx="10" cy="10" rx="3.5" ry="8"/><path d="M2 10h16M3.5 6h13M3.5 14h13"/></g></svg>
          www.marisellacrowephotography-example.com
        </li>
      </ul>
    </div>
  </section>

</body>
</html>
```